Marnie's Fitness Business Cards

I would like my business cards to look expensive and sophisticated using my logo and the information below.

FRONT
Marnie’s Fitness logo

Tag line Become your happiest, healthiest and strongest self

Marnie Pulham Crisp
Personal Trainer

e. marnie@marniesfitness.example

t. 0781350462

w. www.marniesfitness.example

```html
<!DOCTYPE html>
<html lang="en">
<head>
<meta charset="utf-8">
<title>Marnie's Fitness Business Cards</title>
<link rel="stylesheet" href="https://fonts.googleapis.com/css2?family=Questrial&display=swap">
<style>
  :root {
    --canvas: #ffffff;
    --card: #000000;
    --teal: #5cb6bd;
    --stone: #a89f9b;
  }
  * { margin: 0; padding: 0; box-sizing: border-box; }
  html, body {
    width: 1200px; height: 1200px; overflow: hidden;
    background: var(--canvas);
    font-family: "Questrial", "Century Gothic", sans-serif;
  }
  .canvas { position: relative; width: 1200px; height: 1200px; }
  .card {
    position: absolute; width: 480px; height: 839px;
    background: var(--card); text-align: center;
  }
  .card--front { left: 82px; top: 76px; }
  .card--back { left: 654px; top: 210px; }

  .brand { position: absolute; left: 0; right: 0; top: 196px; }
  .brand__circle {
    display: block; margin: 0 auto; width: 72px; height: 72px;
    border: 3px solid var(--teal); border-radius: 50%;
  }
  .brand__name {
    margin-top: 10px; color: var(--teal);
    font-size: 17px; line-height: 20px; letter-spacing: 6px;
    text-transform: uppercase; padding-left: 6px;
  }

  .person { position: absolute; left: 0; right: 0; top: 484px; }
  .person__name {
    color: var(--teal); font-size: 33px; line-height: 38px;
    text-transform: uppercase; letter-spacing: -0.5px; font-weight: 400;
  }
  .person__role { color: var(--stone); font-size: 23px; line-height: 28px; }

  .contact { position: absolute; left: 0; right: 0; top: 645px; list-style: none; }
  .contact__item {
    color: var(--stone); font-size: 20px; line-height: 24px;
    display: flex; justify-content: center; align-items: center; gap: 5px;
  }
  .contact__icon { width: 17px; height: 17px; fill: var(--teal); flex: none; }

  .tagline {
    position: absolute; left: 0; right: 0; top: 634px;
    font-size: 23px; line-height: 28px; text-transform: uppercase;
    color: var(--stone); letter-spacing: -0.3px;
  }
  .tagline .accent { color: var(--teal); }
</style>
</head>
<body>
<main class="canvas">
  <section class="card card--front">
    <div class="brand">
      <span class="brand__circle"></span>
      <p class="brand__name">Marnie’s<br>Fitness</p>
    </div>
    <div class="person">
      <h1 class="person__name">Marnie Pulham Crisp</h1>
      <p class="person__role">Personal Trainer</p>
    </div>
    <ul class="contact">
      <li class="contact__item">
        <svg class="contact__icon" viewBox="0 0 24 24" aria-hidden="true"><path d="M6.6 10.8a15.2 15.2 0 0 0 6.6 6.6l2.2-2.2c.3-.3.7-.4 1-.2 1.1.4 2.3.6 3.6.6.6 0 1 .4 1 1V20c0 .6-.4 1-1 1A17 17 0 0 1 3 4c0-.6.4-1 1-1h3.5c.6 0 1 .4 1 1 0 1.3.2 2.5.6 3.6.1.3 0 .7-.2 1z"/></svg>
        <span>0781350462</span>
      </li>
      <li class="contact__item">
        <svg class="contact__icon" viewBox="0 0 24 24" aria-hidden="true"><path d="M2 5h20v2l-10 6L2 7z"/><path d="M2 9l10 6 10-6v10H2z"/></svg>
        <span>marnie@marniesfitness.example</span>
      </li>
      <li class="contact__item">
        <svg class="contact__icon" viewBox="0 0 24 24" aria-hidden="true"><circle cx="12" cy="12" r="10"/></svg>
        <span>www.marniesfitness.example</span>
      </li>
    </ul>
  </section>

  <section class="card card--back">
    <div class="brand">
      <span class="brand__circle"></span>
      <p class="brand__name">Marnie’s<br>Fitness</p>
    </div>
    <p class="tagline">
      Become your<br>
      <span class="accent">Happiest, healthiest</span><br>
      and <span class="accent">strongest self</span>
    </p>
  </section>
</main>
</body>
</html>
```